Wix web design for healthcare IT consulting firm.

I am looking for a web design built in Wix that it will be easy for me to add or edit content in the future. The web site does not need to be overly complicated, but it should look very polished and professional. I also want to ensure it is mobile device friendly. I do not need any type of on-line purchasing ability. I will eventually do blogs, but for now it is a fairly standard web site with main page, about us, services provided, etc. I would also like a place for potential customers to contact us directly from the web site. I have included a Word document with some content for the web design. I have also included my logo and business card for reference. I would like to utilize similar colors as my business card. One of my primary competitors is https://vonmarlhq.example/

Target Market(s)

Target market could be nursing home CEO, CIO, or other leader at an organization that manages long term care facilities.

Number of Pages Required

5+ page

Colors
876aae

Requirements
Must have
• Be designed to be used in Wix. Use the content I provided to create and make web design. Allow to be viewed on mobile device. Please use similar color structure as attached business card. Please use attached logo in design.

```html
<!DOCTYPE html>
<html lang="en">
<head>
<meta charset="utf-8">
<title>Lumenward Health Solutions — Home</title>
<link rel="stylesheet" href="https://fonts.googleapis.com/css2?family=Oswald:wght@300;400&family=Jost:wght@500&display=swap">
<style>
  :root {
    --header-purple: #a48bc4;
    --brand-panel: #8668b0;
    --nav-active: #7b2ca8;
    --nav-bg: #f1f1f1;
    --nav-text: #7b3aa8;
    --headline: #7a2ea8;
    --white: #ffffff;
    --hero-light: #dfe8ee;
    --hero-mid: #b9c7d1;
    --hero-deep: #6f7b85;
  }
  * { box-sizing: border-box; margin: 0; padding: 0; }
  html, body { width: 1200px; height: 511px; overflow: hidden; background: var(--white); }
  .page { position: relative; width: 1200px; height: 511px; overflow: hidden; }

  .hero-image {
    position: absolute; inset: 0;
    background:
      radial-gradient(ellipse 160px 260px at 600px 420px, var(--hero-deep), rgba(111,123,133,0) 100%),
      linear-gradient(90deg, var(--hero-light) 0%, var(--hero-mid) 35%, #a9b8c3 50%, var(--hero-mid) 65%, var(--hero-light) 100%);
  }

  .site-header {
    position: absolute; top: 0; left: 0; width: 1200px; height: 121px;
    background: linear-gradient(180deg, #a68fc8 0%, var(--header-purple) 100%);
    box-shadow: 0 2px 4px rgba(60, 30, 90, 0.35);
    z-index: 2;
  }
  .brand-panel {
    position: absolute; top: 0; left: 0; width: 294px; height: 121px;
    background: var(--brand-panel);
  }
  .brand-name {
    position: absolute; top: 12px; left: 94px; width: 160px; height: 96px;
    display: flex; align-items: center; justify-content: center; text-align: center;
    font-family: "Oswald", sans-serif; font-weight: 400; font-size: 22px; line-height: 1.1;
    color: var(--white);
  }

  .main-nav {
    position: absolute; top: 58px; left: 624px; height: 45px;
    display: flex; list-style: none;
  }
  .main-nav li {
    height: 45px; display: flex; align-items: center; justify-content: center;
    background: var(--nav-bg); border-left: 1px solid #e2e2e2;
    font-family: "Oswald", sans-serif; font-weight: 300; font-size: 17px;
    color: var(--nav-text); text-transform: uppercase;
  }
  .main-nav li.is-active { background: var(--nav-active); color: var(--white); border-left: none; }

  .hero-card {
    position: absolute; top: 172px; left: 336px; width: 576px; height: 308px;
    background: rgba(255, 255, 255, 0.25);
  }
  .hero-title {
    position: absolute; top: 196px; left: 300px; width: 648px; text-align: center;
    font-family: "Jost", sans-serif; font-weight: 500; font-size: 50px; line-height: 64px;
    color: var(--headline); text-transform: uppercase; letter-spacing: 0.5px;
    text-shadow: 1px 2px 3px rgba(40, 20, 60, 0.45);
  }
  .hero-title span { display: block; white-space: nowrap; }
  .scroll-cue { position: absolute; top: 458px; left: 577px; }
</style>
</head>
<body>
<div class="page">
  <div class="hero-image" role="img" aria-label="Photo of a bright data centre corridor lined with server racks"></div>

  <header class="site-header">
    <div class="brand-panel">
      <div class="brand-name">Lumenward Health Solutions</div>
    </div>
    <ul class="main-nav">
      <li class="is-active" style="width:98px">Home</li>
      <li style="width:104px">About</li>
      <li style="width:123px">Our Team</li>
      <li style="width:116px">Services</li>
      <li style="width:117px">Contact</li>
    </ul>
  </header>

  <div class="hero-card"></div>
  <h1 class="hero-title">
    <span>Increasing the value</span>
    <span>and security of your</span>
    <span>technology</span>
    <span>resources</span>
  </h1>

  <svg class="scroll-cue" width="46" height="36" viewBox="0 0 46 36" aria-hidden="true">
    <polyline points="4,6 23,28 42,6" fill="none" stroke="#ffffff" stroke-width="5"/>
  </svg>
</div>
</body>
</html>
```